Real Estate Company Needs Business Card Designed

We need a business card design for a new real estate company based in Campbell, CA (Silicon Valley). We plan to improve the residential real estate industry by using technology to improve customer experience. We would like to see designs that use a black background. The final design should communicate sophistication and customer service, as well as stability and technology.

Industry/Entity Type

Real Estate

Requirements
Must have
• Black background

```html
<!DOCTYPE html>
<html lang="en">
<head>
<meta charset="utf-8">
<title>Valmere Business Card</title>
<link rel="stylesheet" href="https://fonts.googleapis.com/css2?family=Arimo:wght@400&family=Montserrat:wght@500&display=swap">
<style>
  :root {
    --page-bg: #ffffff;
    --card-bg: #000000;
    --brand-tone: #c8d2ec;
    --text-light: #ffffff;
  }
  html, body {
    margin: 0;
    padding: 0;
    width: 1200px;
    height: 800px;
    overflow: hidden;
    background: var(--page-bg);
  }
  .canvas {
    position: relative;
    width: 1200px;
    height: 800px;
  }
  .business-card {
    position: absolute;
    left: 116px;
    top: 124px;
    width: 968px;
    height: 552px;
    background: var(--card-bg);
    overflow: hidden;
  }
  .brand-name {
    position: absolute;
    left: 0;
    right: 0;
    top: 140px;
    margin: 0;
    text-align: center;
    font-family: "Montserrat", sans-serif;
    font-weight: 500;
    font-size: 104px;
    line-height: 1;
    letter-spacing: 4px;
    color: var(--brand-tone);
  }
  .contact-block {
    position: absolute;
    left: 0;
    right: 0;
    top: 330px;
    text-align: center;
    font-family: "Arimo", sans-serif;
    font-weight: 400;
    color: var(--text-light);
  }
  .contact-block p {
    margin: 0;
  }
  .person-name {
    font-size: 32px;
    line-height: 40px;
  }
  .person-title {
    font-size: 26px;
    line-height: 40px;
  }
  .person-address {
    font-size: 26px;
    line-height: 42px;
    margin-top: 2px !important;
  }
  .person-contact {
    font-size: 26px;
    line-height: 34px;
  }
</style>
</head>
<body>
  <main class="canvas">
    <section class="business-card">
      <h1 class="brand-name">VALMERE</h1>
      <div class="contact-block">
        <p class="person-name">Your Name Here</p>
        <p class="person-title">Title</p>
        <p class="person-address">Address</p>
        <p class="person-contact">Contact Info</p>
      </div>
    </section>
  </main>
</body>
</html>
```